fernbolt website

commerce website to sell cookeries, brackets, mailboxes and to show off homes built. Modern Steel in design see kelvo rides web page to be like: https://www.kelvorides.com/en/ sorry its blue mantis hosting word press divi

must be able to add products to page

Target Market(s)

mainly western states of U.S.

Industry/Entity Type

Building Product

Coding

Coded - Design and coding required

Number of Pages Required

3 page

Font styles to use
Sans Serif

Colors

Designer to choose colors to be used in the design.

Requirements
Must have
• customers to be able to order products from page
• blue mantis hosting word press divi

```html
<!DOCTYPE html>
<html lang="en">
<head>
<meta charset="utf-8">
<title>Fernbolt — Steel Products &amp; Homes Built</title>
<link href="https://fonts.googleapis.com/css2?family=Montserrat:wght@400;500;800;900&family=Oswald:wght@500&family=PT+Sans:wght@400;700&display=swap" rel="stylesheet">
<style>
:root{
  --navy:#4b5c86;
  --orange:#f8990d;
  --ink:#111;
  --text:#666;
  --muted:#8a8a8a;
  --card-bg:#f7f8fa;
  --white:#fff;
}
*{margin:0;padding:0;box-sizing:border-box}
html,body{width:1200px;height:3677px;overflow:hidden;background:var(--white)}
body{position:relative;font-family:"PT Sans",sans-serif;color:var(--text)}
.abs{position:absolute}
.header-shape{left:0;top:0}
.brand{left:76px;top:40px;display:flex;align-items:center;gap:10px;color:var(--white);font-family:"Montserrat",sans-serif;font-weight:800;font-size:24px;letter-spacing:1px}
.brand-dot{width:14px;height:14px;border-radius:50%;background:var(--white)}
.main-nav{left:661px;top:48px;display:flex;gap:28px;font-family:"PT Sans",sans-serif;font-size:14px;letter-spacing:.5px;color:#8b8b8b}
.main-nav .active{color:var(--navy);font-weight:700}
.search-icon{left:1102px;top:45px}
.hero-title{left:78px;top:256px;font-family:"Montserrat",sans-serif;font-weight:900;font-size:53px;line-height:63px;color:var(--ink)}
.hero-text{left:78px;top:403px;width:500px;font-size:16px;line-height:27px}
.btn{display:flex;align-items:center;justify-content:center;background:var(--orange);color:var(--white);font-family:"Montserrat",sans-serif;font-weight:500;font-size:16px;border-radius:0 12px 0 12px}
.photo{display:block}
.hero-photo{left:642px;top:186px;width:482px;height:470px;background:radial-gradient(ellipse at 50% 35%,#e07a24 0%,#5a4a3e 35%,#2e2a28 70%,rgba(255,255,255,0) 72%)}
.section-title{font-family:"Oswald",sans-serif;font-weight:500;font-size:44px;color:var(--ink);text-align:center;width:1200px;left:0;letter-spacing:-.5px}
.product-card{top:963px;width:323px;height:326px;background:var(--navy);border-bottom:5px solid var(--orange);border-radius:0 0 10px 0;text-align:center;overflow:hidden}
.card-notch{position:absolute;left:69px;top:-67px;width:186px;height:134px;border-radius:50%;background:var(--white)}
.product-photo{top:820px;width:140px;height:190px;border-radius:12px}
.product-card h3{position:absolute;top:100px;width:100%;font-family:"Montserrat",sans-serif;font-weight:500;font-size:19px;color:var(--orange)}
.product-card p{position:absolute;top:148px;left:30px;right:30px;font-size:13.5px;line-height:23px;color:var(--white)}
.product-card .arrow{position:absolute;left:147px;top:256px}
.about-photo{left:77px;top:1463px;width:470px;height:318px;background:linear-gradient(180deg,#8a7b72 0%,#d8ccb8 45%,#e6e2da 70%,#8c8a84 100%);clip-path:polygon(0 40%,30% 5%,55% 25%,75% 15%,100% 45%,100% 100%,0 100%)}
.about-title{left:625px;top:1458px;font-family:"Oswald",sans-serif;font-weight:500;font-size:44px;color:var(--ink)}
.about-text{left:625px;top:1537px;width:470px;font-size:14px;line-height:26px;color:var(--muted)}
.offer-card{top:1948px;width:240px;height:456px;background:var(--card-bg);border:1px solid var(--navy);border-radius:0 0 12px 12px;text-align:center}
.offer-photo{position:absolute;left:60px;top:34px;width:120px;height:130px;border-radius:8px}
.offer-icons{position:absolute;top:207px;left:0;width:100%;display:flex;justify-content:center;gap:10px}
.icon-box{width:40px;height:40px;border:1px solid var(--navy);background:var(--white);display:flex;align-items:center;justify-content:center}
.offer-card h4{position:absolute;top:280px;width:100%;font-family:"Montserrat",sans-serif;font-weight:500;font-size:17px;color:#222}
.offer-card p{position:absolute;top:310px;left:20px;right:20px;font-size:13.5px;line-height:23px;color:var(--muted)}
.offer-card .price{position:absolute;top:394px;width:100%;font-family:"Montserrat",sans-serif;font-weight:500;font-size:18px;color:var(--orange)}
.testimonial{left:77px;top:2489px;width:1046px;height:394px;background:var(--navy);border-radius:0 20px 0 20px;text-align:center;color:var(--white)}
.quote-mark{position:absolute;left:494px;top:62px;width:60px;height:60px;background:var(--orange);border-radius:0 14px 0 14px;display:flex;align-items:center;justify-content:center;font-family:"Montserrat",sans-serif;font-weight:900;font-size:52px;line-height:1;padding-top:18px}
.testimonial blockquote{position:absolute;left:200px;right:200px;top:153px;font-size:16px;line-height:27px}
.client-name{position:absolute;top:289px;width:100%;font-family:"Montserrat",sans-serif;font-size:16px;color:var(--orange)}
.client-role{position:absolute;top:317px;width:100%;font-size:13px;color:#dbe0ea}
.slide-prev{position:absolute;left:143px;top:172px}
.slide-next{position:absolute;left:874px;top:172px}
.news-title{left:195px;top:3016px;width:460px;text-align:center;font-family:"Oswald",sans-serif;font-weight:500;font-size:44px;line-height:52px;color:var(--ink)}
.news-text{left:215px;top:3142px;width:420px;text-align:center;font-size:14px;line-height:26px;color:var(--muted)}
.email-field{left:195px;top:3218px;width:459px;height:50px;border:1px solid var(--orange);border-radius:0 14px 0 14px;display:flex;align-items:center;padding-left:26px;font-family:"Montserrat",sans-serif;font-size:15px;color:#333}
.news-photo{left:740px;top:2968px;width:266px;height:417px;background:linear-gradient(160deg,#5d8a69 0%,#3f6b4d 60%,#2f5039 100%);border-radius:40px 40px 6px 6px}
.footer-shape{left:0;top:3460px}
.copyright{left:79px;top:3598px;font-size:13px;color:#e1e5ee}
.footer-nav{left:660px;top:3592px;display:flex;gap:14px;font-family:"PT Sans",sans-serif;font-size:17px;color:var(--white)}
</style>
</head>
<body>

<svg class="abs header-shape" width="650" height="210" viewBox="0 0 650 210" aria-hidden="true">
  <path d="M0 0 H640 C610 40 600 90 575 130 C545 190 495 215 440 195 C380 170 330 110 260 115 C180 120 120 180 60 190 C30 195 10 192 0 190 Z" fill="#4b5c86"/>
</svg>

<div class="abs brand"><span class="brand-dot"></span>FERNBOLT</div>

<nav class="abs main-nav">
  <span class="active">HOME</span><span>PRODUCTS</span><span>HOMES BUILT</span><span>ABOUT</span><span>CONTACT</span>
</nav>
<svg class="abs search-icon" width="22" height="22" viewBox="0 0 22 22" aria-label="Search">
  <circle cx="9" cy="9" r="7" fill="none" stroke="#f8990d" stroke-width="2"/>
  <line x1="14" y1="14" x2="20" y2="20" stroke="#f8990d" stroke-width="2"/>
</svg>

<h1 class="abs hero-title">WELCOME TO<br>FERNBOLT</h1>
<p class="abs hero-text">Lorem ipsum dolor sit amet, consectetur adipiscing elit, sed&nbsp; Duis aute irure dolor in reprehenderit voluptate velit esse cillum dolore eu fugiat nulla pariatur.</p>
<a class="abs btn" style="left:77px;top:511px;width:156px;height:50px">LEARN MORE</a>
<div class="abs photo hero-photo" role="img" aria-label="Hexagonal steel fire pit with mesh lid and burning fire"></div>

<h2 class="abs section-title" style="top:728px">OUR PRODUCTS</h2>

<div class="abs product-card" style="left:77px"><span class="card-notch"></span>
  <h3>STEEL COOKERIES</h3>
  <p>Lorem ipsum dolor sit amet, consectetur adipiscing elit, sed do eiusmod tempor Ut enim ad minim veniam, quis nostrud exercitation commodo consequat.</p>
  <svg class="arrow" width="30" height="10" viewBox="0 0 30 10"><path d="M0 5H28M23 1l5 4-5 4" stroke="#fff" stroke-width="1.6" fill="none"/></svg>
</div>
<div class="abs product-card" style="left:438px"><span class="card-notch"></span>
  <h3>BRACKETS</h3>
  <p>Lorem ipsum dolor sit amet, consectetur adipiscing elit, sed do eiusmod tempor Ut enim ad minim veniam, quis nostrud exercitation commodo consequat.</p>
  <svg class="arrow" width="30" height="10" viewBox="0 0 30 10"><path d="M0 5H28M23 1l5 4-5 4" stroke="#fff" stroke-width="1.6" fill="none"/></svg>
</div>
<div class="abs product-card" style="left:800px"><span class="card-notch"></span>
  <h3>MAIL BOXES</h3>
  <p>Lorem ipsum dolor sit amet, consectetur adipiscing elit, sed do eiusmod tempor Ut enim ad minim veniam, quis nostrud exercitation commodo consequat.</p>
  <svg class="arrow" width="30" height="10" viewBox="0 0 30 10"><path d="M0 5H28M23 1l5 4-5 4" stroke="#fff" stroke-width="1.6" fill="none"/></svg>
</div>
<div class="abs photo product-photo" style="left:168px;background:linear-gradient(180deg,#f29a2e 0%,#2b2b2e 30%,#1e1e22 100%)" role="img" aria-label="Black steel tabletop fire column"></div>
<div class="abs photo product-photo" style="left:530px;background:linear-gradient(135deg,#e4e6ea 0%,#a7abb2 60%,#7d8189 100%)" role="img" aria-label="Polished steel post bracket"></div>
<div class="abs photo product-photo" style="left:892px;background:linear-gradient(180deg,#5a3d33 0%,#2e2522 50%,#1d1a19 100%)" role="img" aria-label="Dark steel mailbox on a post"></div>

<a class="abs btn" style="left:460px;top:1333px;width:271px;height:50px">EXPLORE MORE PRODUCTS</a>

<div class="abs photo about-photo" role="img" aria-label="Two-storey family home with double garage built by the company"></div>
<h2 class="abs about-title">ABOUT COMPANY</h2>
<p class="abs about-text">Lorem ipsum dolor sit amet, consectetur adipiscing elit, sed do eiusmod tempor incididunt ut labore et dolore magna aliqua. Ut enim ad minim veniam, quis nostrud exercitation ullamco laboris nisi ut aliquip ex ea commodo consequat. Duis aute irure dolor in reprehenderit in voluptate velit esse cillum dolore eu fugiat nulla pariatur. Excepteur sint occaecat cupidatat non proident, sunt in culpa qui officia deserunt.</p>
<a class="abs btn" style="left:624px;top:1729px;width:155px;height:51px">LEARN MORE</a>

<h2 class="abs section-title" style="top:1853px">TODAY' S OFFERS</h2>

<div class="abs offer-card" style="left:77px">
  <div class="photo offer-photo" style="background:linear-gradient(160deg,#3f6b52,#1f3b2c)" role="img" aria-label="Green wall-mounted letter box"></div>
  <div class="offer-icons"><span class="icon-box"><svg width="16" height="14" viewBox="0 0 16 14"><path d="M0 1h3l2 8h8l2-6H4" fill="none" stroke="#f8990d" stroke-width="1.6"/><circle cx="6" cy="12" r="1.4" fill="#f8990d"/><circle cx="12" cy="12" r="1.4" fill="#f8990d"/></svg></span><span class="icon-box"><svg width="15" height="13" viewBox="0 0 15 13"><path d="M7.5 13L1 6.5A3.5 3.5 0 017.5 2a3.5 3.5 0 016.5 4.5z" fill="#f8990d"/></svg></span></div>
  <h4>PRODUCT NAME</h4>
  <p>Lorem ipsum dolor sit amet, consectetur adipiscing elit, sed do eiusmod tempor.</p>
  <div class="price">$100.00</div>
</div>
<div class="abs offer-card" style="left:345px">
  <div class="photo offer-photo" style="background:linear-gradient(160deg,#dfe1e4,#8e9299)" role="img" aria-label="Steel angle bracket"></div>
  <div class="offer-icons"><span class="icon-box"><svg width="16" height="14" viewBox="0 0 16 14"><path d="M0 1h3l2 8h8l2-6H4" fill="none" stroke="#f8990d" stroke-width="1.6"/><circle cx="6" cy="12" r="1.4" fill="#f8990d"/><circle cx="12" cy="12" r="1.4" fill="#f8990d"/></svg></span><span class="icon-box"><svg width="15" height="13" viewBox="0 0 15 13"><path d="M7.5 13L1 6.5A3.5 3.5 0 017.5 2a3.5 3.5 0 016.5 4.5z" fill="#f8990d"/></svg></span></div>
  <h4>PRODUCT NAME</h4>
  <p>Lorem ipsum dolor sit amet, consectetur adipiscing elit, sed do eiusmod tempor.</p>
  <div class="price">$100.00</div>
</div>
<div class="abs offer-card" style="left:615px">
  <div class="photo offer-photo" style="background:linear-gradient(180deg,#c9d3d6 0%,#d9c59e 45%,#b99c6e 100%)" role="img" aria-label="Square fire table with glass surround"></div>
  <div class="offer-icons"><span class="icon-box"><svg width="16" height="14" viewBox="0 0 16 14"><path d="M0 1h3l2 8h8l2-6H4" fill="none" stroke="#f8990d" stroke-width="1.6"/><circle cx="6" cy="12" r="1.4" fill="#f8990d"/><circle cx="12" cy="12" r="1.4" fill="#f8990d"/></svg></span><span class="icon-box"><svg width="15" height="13" viewBox="0 0 15 13"><path d="M7.5 13L1 6.5A3.5 3.5 0 017.5 2a3.5 3.5 0 016.5 4.5z" fill="#f8990d"/></svg></span></div>
  <h4>PRODUCT NAME</h4>
  <p>Lorem ipsum dolor sit amet, consectetur adipiscing elit, sed do eiusmod tempor.</p>
  <div class="price">$100.00</div>
</div>
<div class="abs offer-card" style="left:883px">
  <div class="photo offer-photo" style="background:linear-gradient(180deg,#cfd2dc 0%,#9da2b2 55%,#1c1c1e 100%)" role="img" aria-label="Silver rural mailbox on a black post"></div>
  <div class="offer-icons"><span class="icon-box"><svg width="16" height="14" viewBox="0 0 16 14"><path d="M0 1h3l2 8h8l2-6H4" fill="none" stroke="#f8990d" stroke-width="1.6"/><circle cx="6" cy="12" r="1.4" fill="#f8990d"/><circle cx="12" cy="12" r="1.4" fill="#f8990d"/></svg></span><span class="icon-box"><svg width="15" height="13" viewBox="0 0 15 13"><path d="M7.5 13L1 6.5A3.5 3.5 0 017.5 2a3.5 3.5 0 016.5 4.5z" fill="#f8990d"/></svg></span></div>
  <h4>PRODUCT NAME</h4>
  <p>Lorem ipsum dolor sit amet, consectetur adipiscing elit, sed do eiusmod tempor.</p>
  <div class="price">$100.00</div>
</div>

<section class="abs testimonial">
  <div class="quote-mark">“</div>
  <svg class="slide-prev" width="20" height="56" viewBox="0 0 20 56" aria-label="Previous"><path d="M18 2L3 28l15 26" fill="none" stroke="#c9d0e0" stroke-width="1.6"/></svg>
  <blockquote>Lorem ipsum dolor sit amet, consectetur adipiscing elit, sed do eiusmod tempor incididunt ut labore et dolore magna aliqua. Ut enim ad minim veniam, quis nostrud exercitation ullamco laboris nisi ut aliquip ex ea commodo consequat. Duis aute irure voluptate velit esse cillum dolore eu fugiat nulla pariatur.</blockquote>
  <svg class="slide-next" width="20" height="56" viewBox="0 0 20 56" aria-label="Next"><path d="M2 2l15 26L2 54" fill="none" stroke="#c9d0e0" stroke-width="1.6"/></svg>
  <div class="client-name">Client Name</div>
  <div class="client-role">Lorem ipsum dolor</div>
</section>

<h2 class="abs news-title">GET IN TOUCH WITH NEWSLETTER</h2>
<p class="abs news-text">Lorem ipsum dolor sit amet, consectetur adipiscing elit, sed do nisi ut aliquip ex ea commodo consequat.</p>
<div class="abs email-field">Enter Email Address</div>
<a class="abs btn" style="left:336px;top:3282px;width:177px;height:50px">SUBCRIBE NOW</a>
<div class="abs photo news-photo" role="img" aria-label="Green steel parcel drop box holding a cardboard package"></div>

<svg class="abs footer-shape" width="1200" height="217" viewBox="0 0 1200 217" aria-hidden="true">
  <path d="M0 70 C160 10 300 20 430 45 C600 75 720 20 880 8 C1040 -5 1150 40 1200 110 V217 H0 Z" fill="#4b5c86"/>
</svg>
<p class="abs copyright">Copyright © FERNBOLT - 2020 . All Right Reserved.</p>
<nav class="abs footer-nav"><span>Home</span><span>|</span><span>Products</span><span>|</span><span>Homes Built</span><span>|</span><span>About</span><span>|</span><span>Contact</span></nav>

</body>
</html>
```